BEACON CABS

Taxi card design

Need changes very slow in replying to my messages.

Target Market(s)

Customers

Industry/Entity Type

Taxi

Contact Information for Business Card

See previous design

Font styles to use
Sans Serif

Colors
A7469A
B969AE
D3A5CF
EDDBEB
F8F0F9
6B429C
8869AF
B7A5CE
E3DAEB
F3F0F8

Requirements
Nice to have
• We are in the business of looking after people, not just driving vehicles front
Should not have
• Front number 01632 480 480 needs to big big

```html
<!DOCTYPE html>
<html lang="en">
<head>
<meta charset="utf-8">
<title>Beacon Cabs business card</title>
<link rel="stylesheet" href="https://fonts.googleapis.com/css2?family=Open+Sans:wght@400;600;700;800&family=Oswald:wght@500&display=swap">
<style>
  :root {
    --purple-deep: #6B429C;
    --purple-mid: #8869AF;
    --magenta: #A7469A;
    --magenta-soft: #B969AE;
    --lilac: #D3A5CF;
    --lilac-pale: #F8F0F9;
    --lavender: #B7A5CE;
    --lavender-pale: #E3DAEB;
    --ink: #1e1e22;
    --grey-text: #555558;
    --band: #3a3a3d;
    --stage: #2a2a2c;
    --paper: #f6f5f4;
    --white: #ffffff;
  }
  * { box-sizing: border-box; margin: 0; padding: 0; }
  html, body { width: 1200px; height: 783px; overflow: hidden; }
  body {
    background: var(--stage);
    font-family: "Open Sans", sans-serif;
    position: relative;
  }
  .card {
    position: absolute;
    top: 237px;
    width: 540px;
    height: 309px;
    overflow: hidden;
    border-radius: 3px;
  }
  .card--front { left: 40px; background: var(--paper); color: var(--ink); }
  .card--back {
    left: 620px;
    background: linear-gradient(135deg, var(--magenta) 0%, #8a3c94 45%, var(--purple-deep) 100%);
    color: var(--white);
  }

  /* Front */
  .brand {
    position: absolute; left: 34px; top: 28px;
    display: flex; align-items: center; gap: 10px;
  }
  .brand__dot { width: 14px; height: 14px; border-radius: 50%; background: var(--magenta); }
  .brand__name { font-weight: 800; font-size: 38px; letter-spacing: 0.5px; color: var(--ink); line-height: 1; }
  .tagline {
    position: absolute; left: 36px; top: 80px;
    font-size: 15px; letter-spacing: 3.5px; color: var(--grey-text);
  }
  .contacts { position: absolute; left: 36px; top: 118px; list-style: none; }
  .contacts li {
    display: flex; align-items: center; gap: 8px;
    font-size: 12.5px; line-height: 19px; color: var(--ink);
  }
  .contacts svg { width: 13px; height: 13px; flex: none; }
  .divider { position: absolute; left: 36px; top: 182px; width: 205px; height: 1px; background: var(--ink); }
  .address { position: absolute; left: 36px; top: 189px; font-size: 12.5px; line-height: 18px; color: var(--ink); }
  .service { position: absolute; left: 36px; top: 232px; font-size: 13px; color: var(--magenta); font-weight: 600; }
  .band {
    position: absolute; left: 0; bottom: 0; width: 100%; height: 48px;
    background: var(--band);
  }
  .band__phone {
    position: absolute; left: 30px; top: 7px;
    font-weight: 700; font-size: 27px; letter-spacing: 1px; color: var(--white);
  }
  .scene {
    position: absolute; right: 0; bottom: 0; width: 250px; height: 150px;
    background: linear-gradient(90deg, var(--lilac) 0%, var(--lavender-pale) 55%, #a9c2de 100%);
  }
  .services {
    position: absolute; right: 36px; top: 108px; width: 170px;
    background: linear-gradient(135deg, var(--magenta), var(--purple-deep));
    color: var(--white);
    font-family: "Oswald", sans-serif; font-weight: 500;
    font-size: 14.5px; line-height: 17px; text-align: center;
    padding: 10px 8px 12px;
  }
  .services::after {
    content: ""; position: absolute; left: 58px; bottom: -12px;
    border-left: 12px solid transparent; border-right: 0 solid transparent;
    border-top: 12px solid #7d4499;
  }

  /* Back */
  .back-brand {
    position: absolute; left: 0; right: 0; top: 108px;
    display: flex; justify-content: center; align-items: center; gap: 12px;
  }
  .back-brand__dot { width: 16px; height: 16px; border-radius: 50%; background: var(--white); }
  .back-brand__name { font-weight: 800; font-size: 46px; line-height: 1; color: var(--white); }
  .back-numbers {
    position: absolute; left: 0; right: 0; top: 185px;
    text-align: center; font-size: 12.5px; letter-spacing: 0.8px; color: var(--lilac-pale);
  }
</style>
</head>
<body>
  <section class="card card--front">
    <div class="brand">
      <span class="brand__dot"></span>
      <span class="brand__name">Beacon Cabs</span>
    </div>
    <p class="tagline">Established since 1986</p>
    <ul class="contacts">
      <li>
        <svg viewBox="0 0 16 16"><path d="M4 1l2.5 3-1.5 2a8 8 0 0 0 5 5l2-1.5 3 2.5-1.5 2.5C8 15 1 8 1.5 2.5z" fill="var(--magenta)"/></svg>
        0800 555 0 123
      </li>
      <li>
        <svg viewBox="0 0 16 16"><rect x="1" y="3" width="14" height="10" fill="var(--magenta)"/><path d="M1 3l7 6 7-6" stroke="#fff" stroke-width="1.2" fill="none"/></svg>
        beaconcabs@mailbox.co.uk
      </li>
      <li>
        <svg viewBox="0 0 16 16"><circle cx="8" cy="8" r="7" fill="var(--magenta)"/><path d="M1 8h14M8 1c-3 4-3 10 0 14M8 1c3 4 3 10 0 14" stroke="#fff" stroke-width="1" fill="none"/></svg>
        www.beaconcabs.co.uk
      </li>
    </ul>
    <div class="divider"></div>
    <p class="address">Unit 4 Mill Yard<br>Harbour Row Eastwick EW4 2QD</p>
    <p class="service">24/7 Service</p>
    <div class="band"><span class="band__phone">01632 480 480</span></div>
    <div class="scene" role="img" aria-label="Illustration of a chauffeur opening a purple taxi for travellers with luggage outside an airport terminal"></div>
    <div class="services">MINIBUSES<br>AIRPORT TRANSFERS<br>SCHOOL TRANSPORT</div>
  </section>

  <section class="card card--back">
    <div class="back-brand">
      <span class="back-brand__dot"></span>
      <span class="back-brand__name">Beacon Cabs</span>
    </div>
    <p class="back-numbers">01632 960 111 | 01632 960 222 | 01632 960 333</p>
  </section>
</body>
</html>
```